New shirt company looking for a fun and edgy online retail website design

We're a new company looking for a simple yet attractive website to sell shirts/tops to a mostly younger female audience. Our name is Tilvo Shirt Co. and the ArtPavilion logo is uploaded. We're thinking a home page, three separate pages for our shirt "collections", and a contact page/cart page for a grand total of 5 pages. We'd like the website to be coded, easy for the consumer to navigate/shop/checkout, and easy to link to various social media platforms and online websites. For colors, we're aiming for various blues, light grey, and maybe tan/khaki. Our goal is to launch with approximately 20-30 tops/shirts (or 7-10) per page. Please let us know if you have any questions and thank you for helping us! We are very excited to see what is created!

Target Market(s)

Female teens to early twenties

Coding

Coded - Design and coding required

Number of Pages Required

3 page

Font styles to use
Decorative
Script

Colors
cee9f5
85cae6
33a6d7
0393ce
cfdfed
85acd3

Requirements
Must have
• Online shopping/purchasing capabilities, dropdowns to select sizes for each item, easy to add/remove new or seasoned items.

```html
<!DOCTYPE html>
<html lang="en">
<head>
<meta charset="utf-8">
<title>Tilvo Shirt Co. — Home</title>
<link href="https://fonts.googleapis.com/css2?family=Lato:wght@300;400;700&display=swap" rel="stylesheet">
<style>
  :root{
    --navy:#0b4ea2;
    --blue:#0393ce;
    --mid:#33a6d7;
    --sky:#85cae6;
    --pale:#cee9f5;
    --mist:#f2f8fc;
    --orange:#f26a2e;
    --ink:#333;
    --grey:#777;
    --dark:#2f2f2f;
    --darker:#262626;
    --white:#fff;
  }
  *{box-sizing:border-box;margin:0;padding:0}
  html,body{width:1200px;height:2966px;overflow:hidden}
  body{position:relative;font-family:"Lato",sans-serif;color:var(--ink);background:var(--white)}
  .abs{position:absolute}

  /* header */
  .site-header{left:0;top:0;width:1200px;height:103px;background:var(--white)}
  .menu-toggle{left:88px;top:48px;display:flex;align-items:center;gap:18px;font-size:14px;font-weight:700;letter-spacing:.3px}
  .menu-toggle svg{display:block}
  .brand{left:525px;top:24px;width:149px;height:58px;display:flex;align-items:center;justify-content:center;gap:8px;font-size:18px;font-weight:700;color:var(--navy)}
  .brand-dot{width:12px;height:12px;background:var(--navy);border-radius:50%}
  .account-link{right:84px;top:14px;font-size:12px;color:var(--mid)}
  .header-icons{left:992px;top:46px;display:flex;gap:16px}
  .cart-count{left:1100px;top:44px;width:16px;height:16px;border-radius:50%;background:var(--mid);color:var(--white);font-size:10px;text-align:center;line-height:16px}

  /* hero */
  .hero{left:0;top:103px;width:1200px;height:527px;background:linear-gradient(90deg,#7fc6e6 0%,#bfe3f3 55%,#9fd3ec 80%,#7fc6e6 100%)}
  .hero-photo{left:135px;top:103px;width:400px;height:527px;background:linear-gradient(180deg,#b67b5c 0%,#d28a6c 30%,#c44a3a 55%,#3a78b0 75%,#e1b49a 100%);opacity:.85}
  .hero-frame{left:64px;top:151px;width:1071px;height:428px;border:2px solid rgba(255,255,255,.85)}
  .hero-kicker{left:577px;top:240px;font-size:15px;color:var(--blue)}
  .hero-title{left:577px;top:278px;font-size:48px;line-height:57px;color:#333;font-weight:400}
  .btn-pill{background:var(--white);color:var(--orange);border-radius:20px;font-size:15px;text-align:center}
  .hero-cta{left:577px;top:417px;width:132px;height:37px;line-height:37px}
  .hero-arrow{top:350px}
  .dots{display:flex;gap:8px}
  .dots span{width:10px;height:10px;border-radius:50%;border:1.5px solid var(--mid)}
  .dots span.on{background:var(--mid)}
  .hero-dots{left:577px;top:604px}
  .hero-dots span{border-color:var(--white)}
  .hero-dots span.on{background:var(--blue);border-color:var(--blue)}

  /* categories */
  .tile{overflow:hidden}
  .tile-label{position:absolute;height:36px;line-height:36px;padding:0 20px}
  .cat-tees{left:48px;top:658px;width:291px;height:186px;background:linear-gradient(135deg,#9fe0d9,#e9c9b8 60%,#7ed3cb)}
  .cat-shoes{left:48px;top:860px;width:291px;height:187px;background:linear-gradient(135deg,#f5bfd3,#2e3e63 55%,#f1b8cf)}
  .cat-tops{left:354px;top:658px;width:492px;height:389px;background:linear-gradient(100deg,#f6eccc 0%,#cdb25a 35%,#e39b2a 60%,#c8a64f 100%)}
  .cat-acc{left:861px;top:658px;width:292px;height:186px;background:linear-gradient(135deg,#f8c4c9,#2f3b4f 45%,#f6c9cf)}
  .cat-shirts{left:861px;top:860px;width:292px;height:187px;background:linear-gradient(135deg,#2fa5db,#3b8fc7 50%,#2aa0d8)}

  /* featured */
  .featured{left:0;top:1076px;width:1200px;height:1078px;background:var(--mist)}
  .tab{text-align:center;color:var(--navy)}
  .tab b{display:block;font-weight:400;font-size:22px;line-height:24px}
  .tab small{display:block;font-size:13px;letter-spacing:4px}
  .titlebox{border:2px solid var(--navy);border-top-width:2px}
  .titlebox-inner{position:absolute;left:0;right:0;text-align:center;color:var(--navy)}
  .titlebox b{display:block;font-weight:400;font-size:32px;line-height:34px;margin-top:14px}
  .titlebox small{display:block;font-size:17px;letter-spacing:5px;line-height:18px;background:var(--mist);width:140px;margin:0 auto}
  .card-img{border:1.5px solid var(--mid)}
  .p-a{background:linear-gradient(180deg,#fff 0%,#f3ebe4 40%,#222 70%,#fff 100%)}
  .p-b{background:linear-gradient(180deg,#fff 0%,#e03030 45%,#222 85%,#fff 100%)}
  .p-c{background:linear-gradient(180deg,#fafafa 0%,#cfd8e4 45%,#9bb2cc 80%,#f3f3f3 100%)}
  .p-d{background:linear-gradient(180deg,#fff 0%,#e9dacf 45%,#d9c6b8 85%,#fff 100%)}
  .p-e{background:linear-gradient(180deg,#fff 0%,#f05a2a 45%,#6fa8c8 85%,#fff 100%)}
  .card-hover{background:rgba(51,166,215,.78);border:3px solid var(--sky)}
  .hover-btn{width:28px;height:28px;border-radius:50%;background:rgba(255,255,255,.85);display:flex;align-items:center;justify-content:center}
  .p-name{width:232px;text-align:center;font-size:14px;color:#222}
  .p-price{width:232px;text-align:center;font-size:16px;color:var(--navy)}
  .p-price s{font-size:13px;color:#333;margin-left:4px}
  .size-select{left:780px;top:1568px;width:68px;height:23px;border:1px solid var(--mid);border-radius:2px;font-size:13px;color:var(--navy);padding:2px 8px;display:flex;justify-content:space-between;align-items:center}
  .view-all{left:516px;top:2085px;width:167px;height:41px;border:1.5px solid var(--mid);color:var(--blue);font-size:15px;text-align:center;line-height:38px}

  /* testimonial */
  .quote-mark{left:580px;top:2280px}
  .quote-text{left:223px;top:2322px;width:754px;text-align:center;font-size:13px;line-height:16.5px;color:var(--grey)}
  .quote-name{left:0;top:2384px;width:1200px;text-align:center;font-family:"Times New Roman",serif;font-size:14px;color:var(--mid)}
  .avatar{left:537px;top:2408px;width:124px;height:124px;border-radius:50%;background:radial-gradient(circle at 50% 55%,#e2c6b5 0,#d9a99a 35%,#e9a9c8 60%,#ee9fc5 100%)}

  /* newsletter */
  .newsletter{left:0;top:2612px;width:1200px;height:290px;background:var(--dark)}
  .nl-title{left:0;top:2645px;width:1200px;text-align:center;color:var(--white);font-size:17px}
  .nl-text{left:258px;top:2687px;width:684px;text-align:center;color:#bdbdbd;font-size:15px;line-height:19px}
  .nl-input{left:317px;top:2745px;width:463px;height:45px;background:var(--white);border-radius:3px 0 0 3px;color:#aaa;font-size:15px;padding:13px 22px}
  .nl-btn{left:780px;top:2745px;width:102px;height:45px;background:var(--blue);color:var(--white);font-weight:700;font-size:16px;text-align:center;line-height:45px;border-radius:0 3px 3px 0}
  .social{left:493px;top:2829px;display:flex;gap:32px}
  .social span{width:28px;height:28px;border:2px solid #9a9a9a;border-radius:50%}
  .site-footer{left:0;top:2902px;width:1200px;height:64px;background:var(--darker);color:#9a9a9a;font-size:13px;text-align:center;line-height:64px}
</style>
</head>
<body>

<header class="abs site-header">
  <div class="abs menu-toggle">
    <svg width="30" height="24" viewBox="0 0 30 24"><g stroke="#33a6d7" stroke-width="2.5"><line x1="0" y1="2" x2="30" y2="2"/><line x1="0" y1="12" x2="30" y2="12"/><line x1="0" y1="22" x2="30" y2="22"/></g></svg>
    MENU
  </div>
  <div class="abs brand"><span class="brand-dot"></span>Tilvo Shirt Co.</div>
  <a class="abs account-link">My Account</a>
  <div class="abs header-icons">
    <svg width="28" height="28" viewBox="0 0 28 28"><circle cx="11" cy="11" r="9" fill="none" stroke="#111" stroke-width="2.5"/><line x1="18" y1="18" x2="26" y2="26" stroke="#111" stroke-width="2.5"/></svg>
    <svg width="28" height="28" viewBox="0 0 28 28"><path d="M14 25 L3 13 A6 6 0 0 1 14 6 A6 6 0 0 1 25 13 Z" fill="none" stroke="#111" stroke-width="2"/></svg>
    <svg width="28" height="28" viewBox="0 0 28 28"><path d="M4 10 H24 L26 27 H2 Z" fill="none" stroke="#111" stroke-width="2"/><path d="M9 10 V7 A5 5 0 0 1 19 7 V10" fill="none" stroke="#111" stroke-width="2"/></svg>
  </div>
  <div class="abs cart-count">1</div>
</header>

<section class="abs hero">
</section>
<div class="abs hero-photo" role="img" aria-label="Smiling young woman in a patterned summer dress and pink sunglasses making a peace sign"></div>
<div class="abs hero-frame"></div>
<svg class="abs hero-arrow" style="left:92px" width="26" height="50" viewBox="0 0 26 50"><polyline points="24,2 2,25 24,48" fill="none" stroke="#6a7f8c" stroke-width="2"/></svg>
<svg class="abs hero-arrow" style="left:1080px" width="26" height="50" viewBox="0 0 26 50"><polyline points="2,2 24,25 2,48" fill="none" stroke="#6a7f8c" stroke-width="2"/></svg>
<p class="abs hero-kicker">SPRING / SUMMER COLLECTION 2020</p>
<h1 class="abs hero-title">Get up to 30% Off<br>New Arrivals</h1>
<a class="abs btn-pill hero-cta">SHOP NOW</a>
<div class="abs dots hero-dots"><span class="on"></span><span></span><span></span></div>

<section>
  <div class="abs tile cat-tees" role="img" aria-label="Two friends laughing in printed T-shirts"><span class="tile-label btn-pill" style="left:161px;top:132px">T - SHIRTS</span></div>
  <div class="abs tile cat-shoes" role="img" aria-label="Pair of navy sneakers hanging by their laces"><span class="tile-label btn-pill" style="left:167px;top:124px">SHOES</span></div>
  <div class="abs tile cat-tops" role="img" aria-label="Woman in an orange dress carrying a shopping bag"><span class="tile-label btn-pill" style="left:255px;top:324px">TOPS FOR WOMEN</span></div>
  <div class="abs tile cat-acc" role="img" aria-label="Handbags, flowers and perfume on a pink background"><span class="tile-label btn-pill" style="left:143px;top:132px">ACESSERIES</span></div>
  <div class="abs tile cat-shirts" role="img" aria-label="Person in a checked shirt on a blue background">
    <svg class="abs" style="left:119px;top:55px" width="54" height="54" viewBox="0 0 54 54"><circle cx="27" cy="27" r="25" fill="none" stroke="#fff" stroke-width="2"/><line x1="13" y1="27" x2="40" y2="27" stroke="#fff" stroke-width="2"/><polyline points="31,18 40,27 31,36" fill="none" stroke="#fff" stroke-width="2"/></svg>
    <span class="tile-label btn-pill" style="left:92px;top:124px">SHIRTS</span>
  </div>
</section>

<section class="abs featured"></section>
<svg class="abs" style="left:176px;top:1136px" width="26" height="50" viewBox="0 0 26 50"><polyline points="24,2 2,25 24,48" fill="none" stroke="#9aa" stroke-width="2"/></svg>
<svg class="abs" style="left:999px;top:1136px" width="26" height="50" viewBox="0 0 26 50"><polyline points="2,2 24,25 2,48" fill="none" stroke="#9aa" stroke-width="2"/></svg>
<div class="abs tab" style="left:316px;top:1150px;width:120px"><b>NEW</b><small>ARRIVALS</small></div>
<div class="abs titlebox" style="left:497px;top:1118px;width:202px;height:58px">
  <div class="titlebox-inner" style="top:0"><b>FEATURED</b><small>PRODUCTS</small></div>
</div>
<div class="abs tab" style="left:770px;top:1150px;width:150px"><b>LATEST</b><small>COLLECTIONS</small></div>

<div class="abs card-img p-a" style="left:88px;top:1267px;width:232px;height:277px" role="img" aria-label="Model in a black off-shoulder fashion top"></div>
<div class="abs card-img p-b" style="left:351px;top:1267px;width:233px;height:277px" role="img" aria-label="Model in a red sweatshirt and sunglasses"></div>
<div class="abs card-img p-c" style="left:616px;top:1267px;width:233px;height:277px" role="img" aria-label="Model in a printed slogan T-shirt"></div>
<div class="abs card-hover" style="left:616px;top:1267px;width:233px;height:277px">
  <div class="abs hover-btn" style="left:72px;top:230px"><svg width="16" height="10" viewBox="0 0 16 10"><ellipse cx="8" cy="5" rx="7" ry="4" fill="none" stroke="#f26a2e" stroke-width="1.3"/><circle cx="8" cy="5" r="1.8" fill="#f26a2e"/></svg></div>
  <div class="abs hover-btn" style="left:128px;top:230px"><svg width="12" height="14" viewBox="0 0 12 14"><rect x="1" y="4" width="10" height="9" fill="none" stroke="#f26a2e" stroke-width="1.3"/><path d="M3.5 4 V2.5 A2.5 2.5 0 0 1 8.5 2.5 V4" fill="none" stroke="#f26a2e" stroke-width="1.3"/></svg></div>
</div>
<div class="abs card-img p-d" style="left:879px;top:1267px;width:232px;height:277px" role="img" aria-label="Model in a satin camisole top"></div>

<p class="abs p-name" style="left:88px;top:1568px">Fashion Top</p>
<p class="abs p-name" style="left:351px;top:1568px">Red T- Shirt</p>
<p class="abs p-name" style="left:616px;top:1568px;text-align:left">Fashion Top</p>
<div class="abs size-select">Size <svg width="11" height="7" viewBox="0 0 11 7"><polyline points="1,1 5.5,6 10,1" fill="none" stroke="#0b4ea2" stroke-width="1.2"/></svg></div>
<p class="abs p-name" style="left:879px;top:1568px">Fashion Top</p>
<p class="abs p-price" style="left:88px;top:1602px">$256.00<s>$302.00</s></p>
<p class="abs p-price" style="left:351px;top:1602px">$256.00<s>$302.00</s></p>
<p class="abs p-price" style="left:616px;top:1602px;text-align:left">$256.00<s>$302.00</s></p>
<p class="abs p-price" style="left:879px;top:1602px">$256.00<s>$302.00</s></p>

<div class="abs card-img p-d" style="left:88px;top:1655px;width:232px;height:278px" role="img" aria-label="Model in a satin camisole top"></div>
<div class="abs card-img p-e" style="left:351px;top:1655px;width:233px;height:278px" role="img" aria-label="Model in an orange hooded sweatshirt"></div>
<div class="abs card-img p-c" style="left:616px;top:1655px;width:233px;height:278px" role="img" aria-label="Model in a printed slogan T-shirt"></div>
<div class="abs card-img p-a" style="left:879px;top:1655px;width:232px;height:278px" role="img" aria-label="Model in a black off-shoulder top"></div>

<p class="abs p-name" style="left:88px;top:1956px">Black Fashion Top</p>
<p class="abs p-name" style="left:351px;top:1956px">T - shirt</p>
<p class="abs p-name" style="left:616px;top:1956px">Fashion Top</p>
<p class="abs p-name" style="left:879px;top:1956px">Stylish Top</p>
<p class="abs p-price" style="left:88px;top:1990px">$256.00<s>$302.00</s></p>
<p class="abs p-price" style="left:351px;top:1990px">$256.00<s>$302.00</s></p>
<p class="abs p-price" style="left:616px;top:1990px">$256.00<s>$302.00</s></p>
<p class="abs p-price" style="left:879px;top:1990px">$256.00<s>$302.00</s></p>

<div class="abs dots" style="left:577px;top:2049px"><span class="on"></span><span></span><span></span></div>
<a class="abs view-all">VIEW ALL</a>

<section>
  <div class="abs titlebox" style="left:497px;top:2187px;width:202px;height:59px">
    <div class="titlebox-inner" style="top:0"><b>CUSTOMER</b><small style="background:#fff">SAYINGS</small></div>
  </div>
  <svg class="abs quote-mark" width="40" height="30" viewBox="0 0 40 30"><g fill="#0b4ea2"><circle cx="10" cy="20" r="8"/><path d="M2 20 Q2 6 14 2 L15 5 Q8 9 8 16 Z"/><circle cx="30" cy="20" r="8"/><path d="M22 20 Q22 6 34 2 L35 5 Q28 9 28 16 Z"/></g></svg>
  <p class="abs quote-text">Neque porro quisquam est qui dolorem ipsum quia dolor sit amet, consectetur, adipisci velit There is no one who loves pain itself, who seeks after it and wants to have it, simply because it is pain neque porro quisquam est qui dolorem ipsum quia dolor sit amet, consectetur, adi who seeks after it and wants to have it, simply because it is pain.</p>
  <p class="abs quote-name">MIRA DELLANE</p>
  <div class="abs avatar" role="img" aria-label="Portrait of a customer wearing glasses"></div>
  <div class="abs dots" style="left:577px;top:2560px"><span class="on"></span><span></span><span></span></div>
</section>

<section class="abs newsletter"></section>
<h2 class="abs nl-title" style="font-weight:400">NEWSLETTER SIGNUP</h2>
<p class="abs nl-text">Sign up for our e-mail and be the first who know our special offers! Furthermore, we will give a 15% discount on the next order after you sign up.</p>
<div class="abs nl-input">Enter your email ...</div>
<div class="abs nl-btn">Join Us</div>
<div class="abs social" aria-label="Social links"><span></span><span></span><span></span><span></span></div>

<footer class="abs site-footer">© Tilvoshirtcompany 2020. All Rights Reserved</footer>

</body>
</html>
```